Professional Price List Design for Luxury Candle Range (Print-Ready)

This project requires a luxury, calm, high-end price list — not a flyer, not a basic price sheet. I am wanting mainly soft whites, warm creams, beige, subtle gold tones - no bold colours. Layout to be clearly sectioned by candle range; each range must read as a distinct feature, while flowing cohesively on one page (ideally without looking cramped).
Use clean margins and balanced spacing.
Overall layout should resemble a boutique catalogue or luxury menu
Use some of the supplied candle images only, true to size (no distortion)
Elegant, refined typography is essential

If this style or level of refinement is not aligned with your design approach, please do not submit an entry.

Target Market(s)

Individuals interested in wellness, mindfulness, and soulful living

Industry/Entity Type

Wellness & Lifestyle Brand

Colors

Designer to choose colors to be used in the design.

Requirements
Must have
• A design that allows for future updates as new products are released. Contact email clearly visible for ordering
Nice to have
• Some snap shots of each different candle ranges - I have attached individual photos to brief - they DO NOT all have to be included, they are just examples in case you want to use them.
Should not have
• No loud colours. No crowded pricing or tight spacing.

```html
<!DOCTYPE html>
<html lang="en">
<head>
<meta charset="UTF-8">
<title>Hearth Hollow — Price List</title>
<link href="https://fonts.googleapis.com/css2?family=Playfair+Display:wght@400;700&family=Montserrat:ital,wght@0,400;0,600;1,400&display=swap" rel="stylesheet">
<style>
  :root {
    --page: #ffffff;
    --sheet: #f8f7f3;
    --brown: #5a3722;
    --ink: #3a2a20;
    --muted: #6b5d52;
    --olive: #8a8a5a;
    --photo-gold-1: #f1e6d2;
    --photo-gold-2: #c9a262;
    --photo-choc-1: #8d7a6c;
    --photo-choc-2: #3f2a1e;
  }
  * { margin: 0; padding: 0; box-sizing: border-box; }
  html, body { width: 855px; height: 1200px; overflow: hidden; background: var(--page); }
  .canvas { position: relative; width: 855px; height: 1200px; }
  .sheet { position: absolute; left: 49px; top: 65px; width: 754px; height: 1066px; background: var(--sheet); }

  .brand-name {
    position: absolute; left: 0; top: 104px; width: 855px; text-align: center;
    font-family: "Playfair Display", serif; font-weight: 400; font-size: 44px; line-height: 56px;
    color: var(--brown); letter-spacing: 2px;
  }
  .tagline {
    position: absolute; left: 0; top: 203px; width: 855px; text-align: center;
    font-family: "Playfair Display", serif; font-size: 19px; line-height: 26px; color: var(--brown);
  }
  .rule { position: absolute; height: 1px; background: var(--olive); }

  .range-title {
    position: absolute; font-family: "Playfair Display", serif; font-weight: 700;
    font-size: 9.5px; line-height: 12px; letter-spacing: 4.2px; color: var(--brown); text-transform: uppercase;
  }
  .range-desc, .note {
    position: absolute; font-family: "Montserrat", sans-serif; font-style: italic;
    font-size: 6.3px; line-height: 8.4px; color: var(--muted);
  }
  .price-list { position: absolute; list-style: none; }
  .price-list li {
    font-family: "Montserrat", sans-serif; font-size: 7.7px; line-height: 10px; color: var(--ink);
    white-space: nowrap;
  }
  .price-list .item { font-weight: 600; }
  .price-list .price { font-weight: 400; color: var(--muted); }

  .photo { position: absolute; }
  .photo-dessert { left: 125px; top: 535px; width: 278px; height: 185px;
    background: linear-gradient(180deg, var(--photo-choc-1) 0%, #a89484 30%, var(--photo-choc-2) 70%, #b3a89e 100%); }
  .photo-jar { left: 451px; top: 289px; width: 278px; height: 374px;
    background: radial-gradient(ellipse at 50% 60%, var(--photo-gold-2) 0%, #dcc499 40%, var(--photo-gold-1) 75%, #f3f1ee 100%); }

  .email {
    position: absolute; left: 127px; top: 1043px;
    font-family: "Playfair Display", serif; font-size: 14px; line-height: 20px; color: var(--brown);
  }
</style>
</head>
<body>
<div class="canvas">
  <div class="sheet"></div>

  <div class="brand-name">Hearth Hollow</div>
  <p class="tagline">Hand-poured candles created to bring warmth, intention, and beauty living.</p>
  <div class="rule" style="left:124px; top:257px; width:606px;"></div>

  <!-- Left column -->
  <h2 class="range-title" style="left:124px; top:289px;">Core Luxury Range</h2>
  <p class="range-desc" style="left:124px; top:311px; width:282px;">Poured into beautiful, statement vessels, the Core Luxury Range features timeless jars designed to bring warmth, calm, and quiet luxury into your space.</p>
  <ul class="price-list" style="left:124px; top:339px;">
    <li><span class="item">Crystal Riviera – Luxury Jar – 400g</span> <span class="price">— $50</span></li>
  </ul>
  <div class="rule" style="left:123px; top:380px; width:279px;"></div>

  <h2 class="range-title" style="left:126px; top:412px;">Everyday Essentials</h2>
  <p class="range-desc" style="left:127px; top:437px; width:282px;">Simple, comforting candles designed for daily moments of calm and warmth.</p>
  <ul class="price-list" style="left:126px; top:458px;">
    <li><span class="item">Amber Jar – 150g</span> <span class="price">— $20</span></li>
  </ul>
  <div class="rule" style="left:123px; top:502px; width:279px;"></div>

  <div class="photo photo-dessert" role="img" aria-label="Photo of three dessert-style candles in ribbed glass goblets topped with chocolate"></div>

  <h2 class="range-title" style="left:125px; top:752px;">Sugar Row Range</h2>
  <p class="range-desc" style="left:125px; top:772px; width:282px;">A deliciously indulgent collection that looks almost good enough to eat and smells absolutely divine. The Sugar Row Collection fills your space with rich, comforting fragrance — a sweet sensory escape.</p>
  <ul class="price-list" style="left:123px; top:811px;">
    <li style="line-height:15.9px;"><span class="item">Strawberry Milkshake – 235g</span> <span class="price">— $35</span></li>
    <li style="line-height:15.9px;"><span class="item">Chocolate Milkshake – 235g</span> <span class="price">— $35</span></li>
    <li style="line-height:15.9px;"><span class="item">Caramel Popcorn – 295g</span> <span class="price">— $30</span></li>
    <li style="line-height:15.9px;"><span class="item">Iced Coffee – 295g</span> <span class="price">— $30</span></li>
    <li style="line-height:15.9px;"><span class="item">Café Latte – 295g</span> <span class="price">— $30</span></li>
  </ul>
  <div class="rule" style="left:124px; top:918px; width:278px;"></div>

  <p class="note" style="left:126px; top:941px; width:282px;">Hearth Hollow is an evolving collection. New candle creations are introduced regularly, and this price list may be updated to reflect new offerings and limited releases.</p>
  <p class="note" style="left:126px; top:970px; width:282px;">Each Hearth Hollow candle is poured slowly and mindfully, with intention at its core — because what we bring into our homes, and into our lives, truly matters.</p>
  <div class="rule" style="left:123px; top:1017px; width:279px;"></div>

  <div class="email">hello@hearthhollow.com</div>

  <!-- Right column -->
  <div class="photo photo-jar" role="img" aria-label="Photo of a gold textured glass jar candle with a tied label tag"></div>

  <h2 class="range-title" style="left:452px; top:693px;">Signature Inspiration Range</h2>
  <p class="range-desc" style="left:452px; top:716px; width:286px;">These candles are more than scent — they are gentle reminders. Of your worth. Of your strength. Of the importance of choosing moments that nourish you. Created to support presence, self-connection, and intentional living.</p>
  <ul class="price-list" style="left:452px; top:748px;">
    <li style="line-height:17px;"><span class="item">Ashford Amber Jar – Bamboo Lid – 295g</span> <span class="price">— $30</span></li>
    <li style="line-height:17px;"><span class="item">Opal Dome Jar – 200g</span> <span class="price">— $40</span></li>
  </ul>
  <div class="rule" style="left:450px; top:802px; width:279px;"></div>

  <h2 class="range-title" style="left:452px; top:833px;">Baby &amp; Keepsake Range</h2>
  <p class="range-desc" style="left:452px; top:855px; width:286px;">Created to celebrate new life, this range is a soft welcome into the world. Gentle, meaningful candles designed to honour love, beginnings, and the light each little soul brings.</p>
  <ul class="price-list" style="left:452px; top:884px;">
    <li style="line-height:16px;"><span class="item">Hello, Little Light – Ashford Bowl Candle</span> <span class="price">— $55</span></li>
    <li style="line-height:16px;"><span class="item">Hello, Little Light – Ashford Large Jar – 400g</span> <span class="price">— $40</span></li>
  </ul>
  <div class="rule" style="left:451px; top:945px; width:279px;"></div>

  <h2 class="range-title" style="left:452px; top:975px;">Limited Edition Range</h2>
  <p class="range-desc" style="left:452px; top:998px; width:286px;">Small-batch candles released in limited numbers and available for a short time only.</p>
  <ul class="price-list" style="left:452px; top:1013px;">
    <li style="line-height:17px;"><span class="item">Tender Hearts – 200g</span> <span class="price">— $30</span></li>
    <li style="line-height:17px;"><span class="item">Forever Yours – Limited Edition – 400g</span> <span class="price">— $40</span></li>
    <li style="line-height:17px;"><span class="item">Little Cub Lane – Ashford Bowl Candle</span> <span class="price">— $55</span></li>
  </ul>
</div>
</body>
</html>
```